Fundraising Event Logistics and Strategy

We need a web design for our non-profit fundraising event strategy business. We help non-profits streamline gala and 'pre registered' event operations to maximize their funds raised. We would like a simple design, our company colors are dark blue and silver. The design should be clean and also allow for some partner logos. I have attached some current logo collateral. Company is Dana Whitcombe & Co dba GalaPivotry, but neither logo has to be used.
Target Market(s)
Non Profit Organizations
Industry/Entity Type
Business
Number of Pages Required
3 page
Requirements
Must have
- Contact Us Form
- Partner Logos with Links

```html
<!DOCTYPE html>
<html lang="en">
<head>
<meta charset="utf-8">
<title>GalaPivotry</title>
<link href="https://fonts.googleapis.com/css2?family=Open+Sans:wght@400;600;700&display=swap" rel="stylesheet">
<style>
:root{
  --navy:#0c2744;
  --navy-deep:#081c33;
  --blue:#1d4c7a;
  --silver:#c9ced6;
  --green:#74b21f;
  --text:#6b7280;
  --dark:#2a2f36;
  --white:#ffffff;
}
*{margin:0;padding:0;box-sizing:border-box}
html,body{width:738px;height:1200px;overflow:hidden;background:var(--white);font-family:"Open Sans",Arial,sans-serif;color:var(--text)}
.page{position:relative;width:738px;height:1200px}
.hero{position:absolute;left:0;top:0;width:738px;height:345px;background:linear-gradient(180deg,#3d5f86 0%,#6f8fae 45%,#4a5e72 75%,#2c3a48 100%)}
.navbar{position:absolute;left:0;top:0;width:738px;height:44px;background:rgba(8,28,51,.85)}
.brand{position:absolute;left:22px;top:0;width:112px;height:108px;background:var(--navy-deep);display:flex;flex-direction:column;align-items:center;justify-content:center;gap:6px}
.brand-mark{width:30px;height:30px;border:1px solid var(--silver);border-radius:50%}
.brand-name{color:var(--silver);font-size:9px;font-weight:600;text-align:center;line-height:1.3}
.nav{position:absolute;right:14px;top:0;height:44px;display:flex;align-items:center;gap:22px;list-style:none}
.nav li{color:var(--white);font-size:9px;font-weight:600;letter-spacing:.4px}
.hero-title{position:absolute;left:0;width:560px;top:168px;text-align:center;color:var(--white);font-size:24px;font-weight:700;letter-spacing:1px}
.hero-sub{position:absolute;left:0;width:560px;top:200px;text-align:center;color:var(--white);font-size:14px;font-weight:600}
.hero-btn{position:absolute;left:205px;top:236px;width:150px;height:26px;background:var(--green);color:var(--white);font-size:8px;font-weight:700;display:flex;align-items:center;justify-content:center}
.contact-form{position:absolute;left:560px;top:124px;width:146px;display:flex;flex-direction:column;gap:6px}
.field{height:17px;background:var(--white);font-size:7px;color:#999;padding:4px 6px}
.field.message{height:42px}
.submit{height:22px;background:var(--green);color:var(--white);font-size:8px;font-weight:700;display:flex;align-items:center;justify-content:center}
.side-tab{position:absolute;right:0;top:110px;width:22px;height:135px;background:var(--blue);color:var(--white);font-size:7px;font-weight:700;writing-mode:vertical-rl;display:flex;align-items:center;justify-content:center;letter-spacing:1px}
.section-title{position:absolute;left:0;width:738px;text-align:center;color:var(--blue);font-weight:700}
.welcome-title{top:396px;font-size:18px}
.welcome-text{position:absolute;left:210px;width:318px;top:430px;text-align:center;font-size:9px;line-height:1.45;color:var(--text)}
.services-title{top:500px;font-size:14px}
.services-sub{position:absolute;left:0;width:738px;top:522px;text-align:center;font-size:7px}
.service{position:absolute;top:556px;width:143px}
.service-photo{width:143px;height:108px}
.service h3{margin-top:10px;font-size:8px;color:var(--blue);font-weight:700}
.service p{margin-top:3px;font-size:6.5px;line-height:1.4}
.clients-title{top:750px;font-size:14px}
.client-photo{position:absolute;left:110px;top:787px;width:124px;height:124px;border-radius:50%;background:linear-gradient(135deg,#d9d9d9,#8a8a8a)}
.quote-mark{position:absolute;left:262px;top:800px;font-size:22px;color:var(--silver);font-weight:700}
.quote{position:absolute;left:283px;top:812px;width:380px;font-size:7.5px;line-height:1.55;font-style:normal}
.quote-name{position:absolute;left:283px;top:872px;font-size:8px;color:#c0392b;font-weight:600}
.quote-role{position:absolute;left:283px;top:884px;font-size:7px}
.quote-arrows{position:absolute;left:625px;top:880px;font-size:9px;color:#aaa;letter-spacing:6px}
.partners{position:absolute;left:60px;top:964px;width:620px;display:flex;justify-content:space-between;align-items:center}
.partner{display:flex;align-items:center;gap:5px;font-size:11px;font-weight:700;color:var(--dark)}
.partner-dot{width:12px;height:12px;background:var(--dark);border-radius:50%}
.partner-badge{width:50px;height:32px;background:#9aa0a8}
.footer{position:absolute;left:0;top:1028px;width:738px;height:172px;background:var(--navy)}
.footer-col{position:absolute;top:14px}
.footer-col h4{color:var(--white);font-size:8px;font-weight:700;margin-bottom:8px}
.footer-col p,.footer-col li{font-size:6.5px;line-height:1.7;color:#9fb0c4;list-style:none}
.social li{display:flex;align-items:center;gap:6px;margin-bottom:4px}
.social-box{width:10px;height:10px;background:#2b4a70}
.copyright{position:absolute;left:0;width:738px;top:1172px;text-align:center;font-size:6.5px;color:#9fb0c4}
.footer-rule{position:absolute;left:64px;top:1162px;width:610px;height:1px;background:#23405f}
</style>
</head>
<body>
<div class="page">
  <header class="hero" role="img" aria-label="Waterfront city skyline at dusk"></header>
  <div class="navbar">
    <ul class="nav">
      <li>HOME</li><li>ABOUT US</li><li>SERVICES</li><li>TESTIMONIALS</li><li>CLIENTS</li><li>CONTACT US</li>
    </ul>
  </div>
  <div class="brand">
    <div class="brand-mark"></div>
    <div class="brand-name">Dana Whitcombe &amp; Co</div>
  </div>
  <h1 class="hero-title">GALAPIVOTRY</h1>
  <p class="hero-sub">WE ARE INTO NON PROFIT FUNDRAISING EVENT STRATEGY</p>
  <div class="hero-btn">VIEW OUR HISTORY</div>
  <form class="contact-form">
    <div class="field">Name</div>
    <div class="field">Email</div>
    <div class="field">Phone</div>
    <div class="field message">Message</div>
    <div class="submit">SUBMIT NOW</div>
  </form>
  <div class="side-tab">CONTACT NOW</div>

  <h2 class="section-title welcome-title">WELCOME TO GALAPIVOTRY</h2>
  <p class="welcome-text">We are into non-profit fundraising event strategy business. We help non-profits streamline gala and 'pre registered' event operations to maximize their funds raised.</p>

  <h2 class="section-title services-title">OUR SERVICES</h2>
  <p class="services-sub">We plan every gala step by step, from first guest list to final pledge, so your team can focus on the cause.</p>

  <div class="service" style="left:64px">
    <div class="service-photo" role="img" aria-label="Team hands joined together" style="background:linear-gradient(135deg,#b8bcc2,#6d737b)"></div>
    <h3>Lorem Ipsum is a dummy</h3>
    <p>Event planning support that keeps guests, bids and pledges moving smoothly.</p>
  </div>
  <div class="service" style="left:221px">
    <div class="service-photo" role="img" aria-label="Hands working on a laptop" style="background:linear-gradient(135deg,#a9b7c6,#5d6f82)"></div>
    <h3>Lorem Ipsum is a dummy</h3>
    <p>Online registration tools that gather guest details well before the night.</p>
  </div>
  <div class="service" style="left:376px">
    <div class="service-photo" role="img" aria-label="Business charts on a desk" style="background:linear-gradient(135deg,#c7d4e2,#7a93ad)"></div>
    <h3>Lorem Ipsum is a dummy</h3>
    <p>Clear reports that show where funds come from and how to raise more.</p>
  </div>
  <div class="service" style="left:531px">
    <div class="service-photo" role="img" aria-label="Clock face close up" style="background:linear-gradient(135deg,#e2e6ea,#8c96a2)"></div>
    <h3>Lorem Ipsum is a dummy</h3>
    <p>Fast checkout on the night so every guest leaves happy and on time.</p>
  </div>

  <h2 class="section-title clients-title">WHAT OUR CLIENT'S SAY</h2>
  <div class="client-photo" role="img" aria-label="Portrait of a client"></div>
  <div class="quote-mark">&ldquo;</div>
  <p class="quote">Working with this team changed how we run our annual gala. Registration was simple, checkout was quick, and our guests noticed the difference. We raised more than ever before and our volunteers finally had time to enjoy the evening with our supporters.</p>
  <div class="quote-name">Marcus Ellery</div>
  <div class="quote-role">Business Man</div>
  <div class="quote-arrows">&lsaquo; &rsaquo;</div>

  <div class="partners">
    <div class="partner">Fernline</div>
    <div class="partner"><span class="partner-dot"></span>Orbitstay</div>
    <div class="partner-badge"></div>
    <div class="partner-badge"></div>
    <div class="partner-badge"></div>
    <div class="partner-badge"></div>
  </div>

  <footer class="footer">
    <div class="footer-col" style="left:64px;width:200px">
      <h4>ABOUT US</h4>
      <p>We help non-profit teams plan galas and pre registered events that run smoothly and raise more for the causes they care about. Our work covers guest lists, bidding, payments and reports.</p>
    </div>
    <div class="footer-col" style="left:320px">
      <h4>WELCOME</h4>
      <ul><li>Home</li><li>About</li><li>Services</li><li>Testimonials</li><li>Clients</li><li>Contact Us</li></ul>
    </div>
    <div class="footer-col" style="left:455px">
      <h4>INFORMATION</h4>
      <ul><li>Privacy Policy</li><li>Terms &amp; Conditions</li><li>Sitemap</li></ul>
    </div>
    <div class="footer-col social" style="left:570px">
      <h4>FOLLOW US</h4>
      <ul>
        <li><span class="social-box"></span>Friends</li>
        <li><span class="social-box"></span>Updates</li>
        <li><span class="social-box"></span>Photos</li>
        <li><span class="social-box"></span>Network</li>
      </ul>
    </div>
  </footer>
  <div class="footer-rule"></div>
  <p class="copyright">&copy; 2015, GalaPivotry. All rights reserved.</p>
</div>
</body>
</html>
```